Spin Dash 4 Fun business card

Spin Dash 4 Fun is a national UK campaign that promotes the value of play for children. The website has recently undergone a redesign and will soon be going live, this business card design will need to reflect the new website's design and colour scheme, etc.
Key wording/info for inclusion (front)
- Strapline titles
A little Play every day (in caps)
giving you great free play ideas, everyday!
- Logo
Key wording for inclusion (rear)
- Download our free play app - Spin Dash 4 Fun
- Visit our website - www.spindash4fun.co.uk
- To share hints and tips with other parents
www.facebook.com/spindashforfun
- Want to get involved in the campaign? No matter who you are we would love to hear from you! Email - getinvolved@spindashforfun.co.uk
Social media icons
Facebook facebook.com/spindash4fun
Twitter @spindash4fun
Youtube youtube.com/spindashforfun
The target audience is parents of young children up to the age of 12.
Please note that all attached graphics are the property of the Northern Craft & Pastime Guild and must only be used for the purpose of this project.
Updates
Please note the design we are seeking will be in a business card 'shape' but will not be for a specific 'person' or name as such. We are looking for a colourful and modern design which is not 'corporate. Thank you.
Target Market(s)
Industry/Entity Type
Business
Look and feel
Each slider illustrates characteristics of the customer's brand and the style your logo design should communicate.

```html
<!DOCTYPE html>
<html lang="en">
<head>
<meta charset="utf-8">
<title>Spin Dash 4 Fun business card</title>
<link rel="stylesheet" href="https://fonts.googleapis.com/css2?family=Oswald:wght@400;500&family=Open+Sans:wght@400;600&display=swap">
<style>
  :root {
    --backdrop: #e9e7e4;
    --card-white: #ffffff;
    --card-edge: #dcdad6;
    --brand-purple: #6b4c9f;
    --brand-lime: #b8d433;
    --ink-white: #ffffff;
    --ink-soft: #e6def2;
  }
  * { box-sizing: border-box; margin: 0; padding: 0; }
  html, body {
    width: 1200px; height: 896px; overflow: hidden;
    background: var(--backdrop);
  }
  .canvas { position: relative; width: 1200px; height: 896px; }

  .card {
    position: absolute;
    width: 680px; height: 388px;
    background: var(--card-white);
    border: 1px solid var(--card-edge);
    box-shadow: 0 10px 24px rgba(0,0,0,0.18);
    overflow: hidden;
  }
  .card--back { left: 150px; top: 40px; }
  .card--front { left: 370px; top: 468px; display: flex; }

  .brand-name {
    display: flex; align-items: center; gap: 14px;
    font-family: "Oswald", sans-serif; font-weight: 500;
    color: var(--brand-purple); font-size: 44px; letter-spacing: 1px;
    white-space: nowrap;
  }
  .brand-dot {
    width: 30px; height: 30px; border-radius: 50%;
    background: var(--brand-lime); flex: none;
  }

  .card--back .brand-name {
    position: absolute; left: 0; right: 0; top: 100px; justify-content: center;
  }
  .lime-band {
    position: absolute; left: 0; right: 0; top: 250px; height: 62px;
    background: var(--brand-lime);
  }
  .lime-band::before, .lime-band::after {
    content: ""; position: absolute; left: 0; right: 0; height: 2px;
    background: var(--ink-white);
  }
  .lime-band::before { top: 8px; }
  .lime-band::after { bottom: 8px; }

  .front-brand {
    width: 45%; display: flex; align-items: center; justify-content: center;
  }
  .front-brand .brand-name { font-size: 34px; gap: 10px; }
  .front-brand .brand-dot { width: 24px; height: 24px; }

  .info-panel {
    width: 55%; background: var(--brand-purple);
    padding: 40px 28px 28px 32px; color: var(--ink-white);
    font-family: "Open Sans", sans-serif;
  }
  .strapline {
    font-family: "Oswald", sans-serif; font-weight: 400;
    font-size: 22px; letter-spacing: 1.5px; text-transform: uppercase;
    white-space: nowrap;
  }
  .strapline-sub {
    font-size: 12px; color: var(--ink-soft); margin-top: 4px;
  }
  .promo {
    margin-top: 28px; font-size: 13px; line-height: 1.6;
  }
  .promo strong { font-weight: 600; }
  .contact-list { list-style: none; margin-top: 18px; }
  .contact-list li {
    display: flex; align-items: center; gap: 12px;
    font-size: 12px; letter-spacing: 0.3px; margin-bottom: 10px;
    white-space: nowrap;
  }
  .contact-icon {
    width: 18px; height: 18px; background: var(--brand-lime);
    display: flex; align-items: center; justify-content: center; flex: none;
  }
  .contact-icon svg { width: 12px; height: 12px; }
</style>
</head>
<body>
<main class="canvas">

  <section class="card card--back" aria-label="Card back">
    <div class="brand-name"><span class="brand-dot"></span>Spin Dash 4 Fun</div>
    <div class="lime-band"></div>
  </section>

  <section class="card card--front" aria-label="Card front">
    <div class="front-brand">
      <div class="brand-name"><span class="brand-dot"></span>Spin Dash 4 Fun</div>
    </div>
    <div class="info-panel">
      <h1 class="strapline">A Little Play Every Day</h1>
      <p class="strapline-sub">giving you great free play ideas, everyday!</p>
      <p class="promo">
        Download our free play app – <strong>Spin Dash 4 Fun</strong><br>
        Visit our website – <strong>www.spindash4fun.co.uk</strong>
      </p>
      <ul class="contact-list">
        <li><span class="contact-icon"></span>facebook.com/spindash4fun</li>
        <li><span class="contact-icon"></span>@spindash4fun</li>
        <li><span class="contact-icon"></span>youtube.com/spindashforfun</li>
        <li>
          <span class="contact-icon"><svg viewBox="0 0 12 12"><rect x="1" y="3" width="10" height="7" fill="#6b4c9f"/><path d="M1 3l5 4 5-4" stroke="#b8d433" fill="none"/></svg></span>
          getinvolved@spindashforfun.co.uk
        </li>
      </ul>
    </div>
  </section>

</main>
</body>
</html>
```